Brisk Meadow Builders needs a product brochure

We need a new flyer for our Patio Perch Lounge. Here is some of the copy your will need.
"Turn your back yard into the ultimate entertianment venue with the stunning Patio Perch Lounge!"
"Entertain family & friends in your very own back yard!"
"Available with or without solar and comes in a variety of colors"
"The Patio Perch Lounge measures 5' deep by 10' wide and is 9'-6" at it's highest point"
"Constructed with treated 4x4's, primed then painted with Thornby Calder best exterior paint for years of care free enjoyment. Also, Marlow Pendt Keystead shingles are dimensional, have a 25 year warranty and are rated for 150 mph winds!"
"TV Mount included. Shelves and TV are sold separately"
There also needs to be a box where we can add the price into later. The price can change from time to time due to material cost fluctuation.
Look and feel
Each slider illustrates characteristics of the customer's brand and the style your logo design should communicate.

```html
<!DOCTYPE html>
<html lang="en">
<head>
<meta charset="utf-8">
<title>Brisk Meadow Builders – Patio Perch Lounge Flyer</title>
<link href="https://fonts.googleapis.com/css2?family=Ubuntu:wght@500;700&family=Lato:ital,wght@0,400;0,700;1,400&display=swap" rel="stylesheet">
<style>
  :root {
    --green: #55a03a;
    --green-dark: #3f8a2a;
    --orange: #f6ad1f;
    --orange-deep: #e99a12;
    --ink: #2a2a22;
    --ink-green: #23301a;
    --white: #ffffff;
    --accent-green: #4b9a2c;
  }
  * { margin: 0; padding: 0; box-sizing: border-box; }
  html, body { width: 902px; height: 1200px; overflow: hidden; background: var(--white); }
  .flyer { position: relative; width: 902px; height: 1200px; overflow: hidden; font-family: "Lato", sans-serif; color: var(--ink); }
  .shapes, .hero-photo { position: absolute; left: 0; top: 0; }

  .brand { position: absolute; left: 60px; top: 60px; width: 320px; display: flex; align-items: center; justify-content: center; gap: 14px; }
  .brand-dot { width: 46px; height: 46px; border-radius: 50%; background: var(--green); flex: none; }
  .brand-name { font-family: "Ubuntu", sans-serif; font-weight: 700; color: var(--orange); font-size: 32px; line-height: 1.02; text-transform: uppercase; }

  .headline { position: absolute; left: 46px; top: 250px; width: 380px; font-family: "Ubuntu", sans-serif; font-weight: 700; }
  .headline .lead { color: var(--white); font-size: 48px; line-height: 1.05; }
  .headline .sub { color: var(--ink-green); font-size: 21px; line-height: 1.28; margin-top: 14px; }
  .headline .product { color: var(--white); font-size: 40px; line-height: 1.05; margin-top: 16px; }
  .headline .product-big { color: var(--white); font-size: 70px; line-height: 0.95; }

  .family-band { position: absolute; left: 356px; top: 620px; width: 540px; font-family: "Ubuntu", sans-serif; font-weight: 700; font-size: 24px; line-height: 1.3; color: var(--ink); text-transform: uppercase; }

  .photo-circle { position: absolute; left: 40px; top: 582px; width: 296px; height: 296px; border-radius: 50%; border: 7px solid var(--white); background: radial-gradient(circle at 45% 40%, #8a8676 0%, #5e5a4e 45%, #2e2b26 100%); box-shadow: 0 3px 8px rgba(0,0,0,.25); }

  .features { position: absolute; left: 408px; top: 734px; width: 480px; }
  .feature { display: flex; gap: 8px; font-style: italic; font-size: 16.5px; line-height: 1.5; margin-bottom: 8px; }
  .feature svg { flex: none; margin-top: 3px; }
  .specs { padding-left: 32px; font-size: 15.5px; line-height: 1.2; margin-top: 14px; }
  .specs p { margin-bottom: 16px; }
  .specs .highlight { color: var(--accent-green); font-weight: 700; }

  .detail-photo { position: absolute; top: 965px; height: 100px; }
  .detail-shelf { left: 452px; width: 198px; background: linear-gradient(135deg, #8b5a2f 0%, #5a3a22 55%, #c22d45 100%); }
  .detail-mount { left: 658px; width: 208px; background: linear-gradient(135deg, #3a3a3a 0%, #8d6a44 55%, #b98a58 100%); }

  .mount-note { position: absolute; left: 470px; top: 1086px; width: 420px; font-size: 14px; color: var(--ink); }

  .price-label { position: absolute; left: 0; top: 926px; width: 410px; text-align: center; font-family: "Ubuntu", sans-serif; font-weight: 700; font-size: 17.5px; line-height: 1.4; color: var(--ink); text-transform: uppercase; }

  .footer { position: absolute; left: 0; top: 1124px; width: 902px; height: 76px; background: var(--green); display: flex; align-items: center; padding-left: 40px; color: var(--white); }
  .footer-item { display: flex; align-items: center; gap: 10px; }
  .footer-phone { font-family: "Ubuntu", sans-serif; font-weight: 700; font-size: 25px; }
  .footer-address { font-family: "Ubuntu", sans-serif; font-weight: 500; font-size: 13px; line-height: 1.3; }
  .footer-web { font-family: "Ubuntu", sans-serif; font-weight: 700; font-size: 15px; }
  .footer-divider { width: 2px; height: 44px; background: rgba(255,255,255,.85); margin: 0 20px; }
</style>
</head>
<body>
<div class="flyer">
  <svg class="shapes" width="902" height="1200" viewBox="0 0 902 1200" aria-hidden="true">
    <rect width="902" height="1200" fill="#ffffff"/>
    <polygon points="0,225 450,225 400,1004 0,1004" fill="var(--green)"/>
    <polygon points="476,0 493,0 335,603 318,603" fill="var(--orange)"/>
    <polygon points="380,697 902,697 902,1110 420,1110" fill="#ffffff"/>
    <polygon points="378,697 394,697 434,1112 418,1112" fill="var(--orange)"/>
    <polygon points="418,1078 902,1078 902,1114 422,1114" fill="var(--orange)"/>
    <polygon points="0,913 404,913 414,1004 0,1004" fill="var(--orange)"/>
    <polygon points="0,1004 414,1004 420,1124 0,1124" fill="#ffffff"/>
    <polygon points="262,605 902,605 902,700 290,700" fill="rgba(0,0,0,.12)"/>
    <polygon points="258,601 902,601 902,695 286,695" fill="var(--orange)"/>
  </svg>

  <svg class="hero-photo" width="902" height="605" viewBox="0 0 902 605" role="img" aria-label="Photo of the Patio Perch Lounge: a dark gabled outdoor bar with a wall-mounted TV, guests on bar stools, pumpkins and a dog on a paved patio">
    <defs>
      <linearGradient id="heroTone" x1="0" y1="0" x2="0" y2="1">
        <stop offset="0" stop-color="#7f9a55"/>
        <stop offset="0.35" stop-color="#3a3a3d"/>
        <stop offset="0.7" stop-color="#4a4744"/>
        <stop offset="1" stop-color="#a7a39c"/>
      </linearGradient>
    </defs>
    <polygon points="493,0 902,0 902,603 335,603" fill="url(#heroTone)"/>
  </svg>

  <div class="brand">
    <span class="brand-dot"></span>
    <span class="brand-name">Brisk Meadow<br>Builders</span>
  </div>

  <h1 class="headline">
    <span class="lead">TURN YOUR<br>BACK YARD</span>
    <div class="sub">INTO THE ULTIMATE<br>ENTERTIANMENT VENUE<br>WITH THE STUNNING</div>
    <div class="product">PATIO PERCH</div>
    <div class="product-big">LOUNGE!</div>
  </h1>

  <h2 class="family-band">Entertain family &amp; friends in<br>your very own back yard!</h2>

  <div class="photo-circle" role="img" aria-label="Photo of a guest at the lounge bar opening a drink"></div>

  <div class="features">
    <div class="feature">
      <svg width="18" height="18" viewBox="0 0 18 18"><circle cx="9" cy="9" r="7.5" fill="none" stroke="var(--green)" stroke-width="1.8"/><path d="M5 9.2l2.8 2.8L14.5 4" fill="none" stroke="var(--green)" stroke-width="2.2" stroke-linecap="round"/></svg>
      <span>Available with or without solar and comes in a variety of colors</span>
    </div>
    <div class="feature">
      <svg width="18" height="18" viewBox="0 0 18 18"><circle cx="9" cy="9" r="7.5" fill="none" stroke="var(--green)" stroke-width="1.8"/><path d="M5 9.2l2.8 2.8L14.5 4" fill="none" stroke="var(--green)" stroke-width="2.2" stroke-linecap="round"/></svg>
      <span>The Patio Perch Lounge measures 5' deep by 10' wide and is 9'-6" at it's highest point</span>
    </div>
    <div class="specs">
      <p>Constructed with treated 4x4's, primed then painted with Thornby Calder best exterior paint for years of care free enjoyment.</p>
      <p>Also, Marlow Pendt Keystead shingles are dimensional, have a <span class="highlight">25 year warranty and are rated for 150 mph winds!</span></p>
    </div>
  </div>

  <div class="detail-photo detail-shelf" role="img" aria-label="Photo of the wooden wine shelf and red cooler inside the lounge"></div>
  <div class="detail-photo detail-mount" role="img" aria-label="Photo of the wooden bar top and TV mount detail"></div>

  <p class="mount-note">TV Mount included. Shelves and TV are sold separately</p>

  <div class="price-label">The price<br>of the stunning<br>Patio Perch Lounge!</div>

  <footer class="footer">
    <div class="footer-item">
      <svg width="30" height="30" viewBox="0 0 30 30" aria-hidden="true"><circle cx="15" cy="15" r="13" fill="none" stroke="#fff" stroke-width="2"/><path d="M10.5 8.5l2.5-.5 1.5 3.5-1.8 1.3a8 8 0 0 0 4.5 4.5l1.3-1.8 3.5 1.5-.5 2.5c-.3 1-1.5 1.5-2.5 1.2A12 12 0 0 1 9.3 11c-.3-1 .2-2.2 1.2-2.5z" fill="#fff"/></svg>
      <span class="footer-phone">555-418-2093</span>
    </div>
    <span class="footer-divider"></span>
    <div class="footer-item">
      <svg width="14" height="18" viewBox="0 0 14 18" aria-hidden="true"><path d="M7 1a6 6 0 0 0-6 6c0 4.5 6 10 6 10s6-5.5 6-10a6 6 0 0 0-6-6z" fill="none" stroke="#fff" stroke-width="1.8"/><circle cx="7" cy="7" r="2" fill="#fff"/></svg>
      <span class="footer-address">2750 Larkspur Bend Rd,<br>Fenwick Hill, SC 29000</span>
    </div>
    <span class="footer-divider"></span>
    <div class="footer-item">
      <svg width="18" height="18" viewBox="0 0 18 18" aria-hidden="true"><g fill="none" stroke="#fff" stroke-width="1.4"><circle cx="9" cy="9" r="7.5"/><ellipse cx="9" cy="9" rx="3.2" ry="7.5"/><path d="M1.5 9h15M2.8 5h12.4M2.8 13h12.4"/></g></svg>
      <span class="footer-web">www.briskmeadowbuilders.com</span>
    </div>
  </footer>
</div>
</body>
</html>
```